Tire trade

Hello, I would like to make A5 flyers for my garage, with the 'varek tires' logo.
Registration: Sale and fitting of tires of all brands (also ordered by you) Guarding of your tires

Target Market(s)

All motorists in my area

Industry/Entity Type

Vente de pneus

Font styles to use
Serif

Colors
EE7325
F08F49
F5BC92
FAE3D3
FDF4ED

Requirements
Must have
• My logo, the place (Val-d'Illiez)
Nice to have
• Simple and eye-catching
Should not have
• pink

```html
<!DOCTYPE html>
<html lang="en">
<head>
<meta charset="utf-8">
<title>varek tires – Tire Flyer, Val-d'Illiez</title>
<link href="https://fonts.googleapis.com/css2?family=Roboto+Slab:wght@300;400;500;700;800;900&display=swap" rel="stylesheet">
<style>
  :root{
    --orange:#EE7325;
    --orange-mid:#F08F49;
    --peach:#F5BC92;
    --cream:#FAE3D3;
    --paper:#FDF9F6;
    --amber:#F8AE2E;
    --ink:#111111;
    --grey:#555555;
    --night:#1c1d22;
    --white:#ffffff;
    --dots:#f5d03a;
  }
  *{margin:0;padding:0;box-sizing:border-box}
  html,body{width:839px;height:1200px;overflow:hidden;background:var(--paper)}
  body{font-family:"Roboto Slab",serif;color:var(--ink)}
  .flyer{position:relative;width:839px;height:1200px;overflow:hidden;background:var(--paper)}

  .hero-photo{position:absolute;left:0;top:0;width:839px;height:617px;
    background:radial-gradient(ellipse at 45% 70%, #5e606b 0%, #40424c 35%, #2a2b31 70%, var(--night) 100%)}
  .stack-photo{position:absolute;left:480px;top:400px;width:359px;height:270px;
    background:radial-gradient(ellipse 55% 50% at 45% 48%, #b9bbc1 0%, #6c6e76 28%, #303136 55%, rgba(40,41,46,.85) 72%, rgba(40,41,46,0) 100%)}

  .brand{position:absolute;left:76px;top:44px;display:flex;align-items:center;gap:7px;color:var(--white);
    font-weight:800;font-size:22px;letter-spacing:.3px;line-height:1}
  .brand-dot{width:12px;height:12px;border-radius:50%;background:var(--white)}
  .brand-phone{position:absolute;left:95px;top:70px;color:var(--white);font-size:9px;font-weight:700;line-height:11px}

  .headline{position:absolute;left:0;width:839px;text-align:center;color:var(--white);font-weight:700;line-height:1}
  .headline.intro{top:124px;font-size:40px}
  .headline.main{top:190px;font-size:58px;font-weight:900;letter-spacing:1px}
  .headline.sub{top:274px;font-size:42px}

  .offer-badge{position:absolute;left:1px;top:544px;width:134px;height:134px;border-radius:50%;
    background:linear-gradient(135deg,var(--amber) 0%,var(--orange) 100%);text-align:center;color:var(--ink);font-weight:800}
  .offer-badge .small{display:block;margin-top:28px;font-size:18px;line-height:1}
  .offer-badge .big{display:block;font-size:28px;line-height:1;margin-top:4px}

  .products{position:absolute;left:43px;top:712px;width:796px;height:159px}
  .product{position:absolute;top:0;width:259px;height:159px}
  .product .panel{position:absolute;left:113px;top:0;width:160px;height:159px;background:var(--white)}
  .product .tire-photo{position:absolute;left:145px;top:10px;width:96px;height:140px;
    background:radial-gradient(ellipse 50% 50% at 50% 50%, #5a5a5a 0%, #1f1f1f 55%, rgba(31,31,31,.7) 75%, rgba(255,255,255,0) 100%)}
  .product h3{position:absolute;left:0;top:12px;font-size:15px;font-weight:800;white-space:nowrap;line-height:1}
  .product .lead{position:absolute;left:0;top:34px;width:142px;font-size:7.6px;line-height:9.6px;font-weight:500;color:#333}
  .product .note{position:absolute;left:0;top:99px;width:142px;font-size:7.6px;line-height:9.6px;font-weight:300;color:var(--grey)}
  .product .price{position:absolute;left:0;top:129px;font-size:14px;font-weight:800;color:var(--orange);line-height:1}

  .info-title{position:absolute;left:0;top:921px;width:839px;text-align:center;font-size:17.5px;font-weight:600;line-height:1.1}
  .info-copy{position:absolute;left:88px;top:949px;width:663px;text-align:center;font-size:12px;line-height:14.5px;font-weight:300;color:#444}

  .cta-band{position:absolute;left:0;top:1011px;width:839px;height:68px;
    background:linear-gradient(90deg,var(--amber) 0%,var(--orange-mid) 60%,var(--orange) 100%);
    display:flex;align-items:center;justify-content:center;font-size:23px;font-weight:800;letter-spacing:.2px}

  .contact{position:absolute;left:44px;top:1110px}
  .contact .label{font-size:14px;font-weight:700;line-height:1.2}
  .contact .email{font-size:16px;color:var(--orange);font-weight:400;margin-top:2px;line-height:1.2}
  .shop-button{position:absolute;left:293px;top:1112px;width:247px;height:38px;background:var(--amber);
    display:flex;align-items:center;justify-content:center;font-size:16px;font-weight:800}
  .web{position:absolute;left:590px;top:1114px;width:180px;text-align:center}
  .web .url{font-size:12px;line-height:1.2}
  .web .visit{font-size:16px;font-weight:800;color:var(--orange);margin-top:3px;line-height:1.2}

  .deco{position:absolute}
  .wave{position:absolute;left:0;top:1165px}
</style>
</head>
<body>
<div class="flyer">
  <div class="hero-photo" role="img" aria-label="Dark smoky studio scene with alloy-wheel tires"></div>

  <svg class="deco" style="left:806px;top:0" width="33" height="40" aria-hidden="true">
    <g fill="var(--dots)"><circle cx="3" cy="2" r="1.3"/><circle cx="15" cy="2" r="1.3"/><circle cx="27" cy="2" r="1.3"/>
    <circle cx="3" cy="14" r="1.3"/><circle cx="15" cy="14" r="1.3"/><circle cx="27" cy="14" r="1.3"/>
    <circle cx="3" cy="26" r="1.3"/><circle cx="15" cy="26" r="1.3"/><circle cx="27" cy="26" r="1.3"/>
    <circle cx="3" cy="38" r="1.3"/><circle cx="15" cy="38" r="1.3"/><circle cx="27" cy="38" r="1.3"/></g>
  </svg>
  <svg class="deco" style="left:0;top:355px" width="20" height="45" aria-hidden="true">
    <g fill="var(--dots)"><circle cx="3" cy="4" r="1.3"/><circle cx="16" cy="4" r="1.3"/><circle cx="3" cy="16" r="1.3"/><circle cx="16" cy="16" r="1.3"/><circle cx="3" cy="28" r="1.3"/><circle cx="16" cy="28" r="1.3"/><circle cx="3" cy="40" r="1.3"/><circle cx="16" cy="40" r="1.3"/></g>
  </svg>
  <svg class="deco" style="left:192px;top:519px" width="34" height="34" aria-hidden="true"><circle cx="17" cy="17" r="14.5" fill="none" stroke="#7a4a32" stroke-width="2"/></svg>
  <svg class="deco" style="left:418px;top:578px" width="32" height="32" aria-hidden="true"><path d="M16 2v28M2 16h28" stroke="#555862" stroke-width="6"/></svg>

  <div class="brand"><span class="brand-dot"></span>varek tires</div>
  <div class="brand-phone">079/555.01.23 · Val-d'Illiez</div>

  <div class="headline intro">Get Your Tire</div>
  <div class="headline main">ALWAYS READY</div>
  <div class="headline sub">All Brand</div>

  <div class="stack-photo" role="img" aria-label="Stack of winter tires with silver alloy rim in snow"></div>

  <div class="offer-badge"><span class="small">BUY 4</span><span class="big">GET 1<br>FREE !</span></div>

  <svg class="deco" style="left:753px;top:668px" width="44" height="28" aria-hidden="true"><path d="M22 2L42 26H2Z" fill="none" stroke="var(--peach)" stroke-width="1.3"/></svg>

  <div class="products">
    <div class="product" style="left:0">
      <div class="panel"></div>
      <div class="tire-photo" role="img" aria-label="Summer tire on black alloy wheel"></div>
      <h3>SUMMER TIRES</h3>
      <p class="lead">Sale and fitting of summer tires of all brands. Good grip on dry and wet roads, low noise and long wear. We also fit tires that you ordered yourself, quickly and at a fair price in our garage.</p>
      <p class="note">Fitting and balancing included, done while you wait</p>
      <p class="price">PRICE : $ 99</p>
    </div>
    <div class="product" style="left:259px">
      <div class="panel"></div>
      <div class="tire-photo" role="img" aria-label="Winter tire on black alloy wheel"></div>
      <h3>WINTER TIRES</h3>
      <p class="lead">Sale and fitting of winter tires of all brands. Sure grip on snow and ice for the mountain roads around the valley. Order through us or bring your own set and we fit it for you.</p>
      <p class="note">Fitting and balancing included, done while you wait</p>
      <p class="price">PRICE : $ 99</p>
    </div>
    <div class="product" style="left:518px">
      <div class="panel"></div>
      <div class="tire-photo" role="img" aria-label="All-season tire on black alloy wheel"></div>
      <h3>TIRE STORAGE</h3>
      <p class="lead">Guarding of your tires between seasons. We keep your set clean, dry and safe in our store, check wear and pressure, then fit it again on your car when the season changes.</p>
      <p class="note">Storage per set of four tires for one full season</p>
      <p class="price">PRICE : $ 99</p>
    </div>
  </div>

  <h2 class="info-title">SALE, FITTING AND STORAGE OF TIRES IN VAL-D'ILLIEZ</h2>
  <p class="info-copy">Tires of all brands for every motorist in the area, also tires ordered by you. We fit them, balance them and guard your seasonal set until you need it again. Visit our garage in Val-d'Illiez.</p>
  <svg class="deco" style="left:711px;top:948px" width="32" height="32" aria-hidden="true"><circle cx="16" cy="16" r="14" fill="none" stroke="var(--cream)" stroke-width="2"/></svg>

  <div class="cta-band">BUY ONLINE PICK-UP AT OUR STORE OR CALL 09055510</div>

  <svg class="deco" style="left:2px;top:1079px" width="26" height="22" aria-hidden="true"><path d="M1 1H25L13 21Z" fill="none" stroke="var(--peach)" stroke-width="1.2"/></svg>

  <div class="contact">
    <div class="label">For More Information</div>
    <div class="email">info@varektires.com</div>
  </div>
  <div class="shop-button">BUY OUR PRODUCTS</div>
  <div class="web">
    <div class="url">www.varektires.com</div>
    <div class="visit">VISIT OUR WEBSITE</div>
  </div>

  <svg class="deco" style="left:778px;top:1112px" width="56" height="14" aria-hidden="true"><g fill="var(--cream)"><circle cx="7" cy="7" r="6"/><circle cx="26" cy="7" r="6"/><circle cx="45" cy="7" r="6"/></g></svg>
  <svg class="deco" style="left:528px;top:1163px" width="28" height="26" aria-hidden="true"><path d="M1 1H27L14 25Z" fill="none" stroke="var(--peach)" stroke-width="1.2"/></svg>
  <svg class="deco" style="left:322px;top:1175px" width="100" height="6" aria-hidden="true"><g fill="var(--dots)"><circle cx="3" cy="3" r="1.6"/><circle cx="24" cy="3" r="1.6"/><circle cx="45" cy="3" r="1.6"/><circle cx="66" cy="3" r="1.6"/><circle cx="87" cy="3" r="1.6"/></g></svg>

  <svg class="wave" width="839" height="35" viewBox="0 0 839 35" aria-hidden="true">
    <path d="M0 10 Q420 35 839 10 V35 H0Z" fill="var(--peach)"/>
    <path d="M0 20 Q420 42 839 20 V35 H0Z" fill="var(--cream)"/>
  </svg>
</div>
</body>
</html>
```